Environmental and Industrial Services Company Needs Brochure Design

We need a new brochure design for an established company that services the Southeastern United States. It is a highly diversified company that centers around Environmental and Industrial Services. The Environmental side revolved around emergency chemical and spill response, HAZMAT, hazardous/ non hazardous waste management, wastewater treatment, and remediation services (cleaning up contaminated sites). And the Industrial side utilizes heavy equipment like vacuum trucks and hydroblasters to clean process equipment inside of factories and manufacturing facilities. Predominantly our clients are large industrial clients, commercial clients, and the government. The people who would see the brochure are decision makers; engineers, project managers, procurement heads for large companies. These are serious and educated people who are looking for the best.

The designs should incorporate our colors and I welcome you to use any of the pictures from our website www.kdlpurex.com EXCLUSIVELY FOR THIS PROJECT, of course. This brochure should communicate professionalism, confidence, stability, and portray the kind of company who efficiently manages complicated issues. Our site gives a better kind of idea of the branding we want to extend into the brochure and I caution any designer to NOT allow the environmental aspect of our company to lead them to design brochures more fitting for Green Tech companies or Alternative Energy.

Target Market(s)

Engineers, Factory Managers, Project Managers, Consultants, Heads of Large Companies, Service Managers

Industry/Entity Type

Industrial

Requirements
Must have
• The brochure must
-Be divided like the services section of our website w/ categories in this order:
-Industrial Services, Waste Management, Remediation Services, Emergency Response, Marine Services, Stormwater Services
-Owing to the large info in these sections, I'd recommend separate pages or tabs
-Incorporate our colors
-Use photos from the site

```html
<!DOCTYPE html>
<html lang="en">
<head>
<meta charset="utf-8">
<title>KDL Environmental – Industrial Services Brochure Spread</title>
<link rel="stylesheet" href="https://fonts.googleapis.com/css2?family=Source+Sans+3:wght@400;600;700&family=Fira+Sans+Extra+Condensed:wght@600&display=swap">
<style>
  :root{
    --navy:#0b4586;
    --blue:#1d5c9e;
    --sky:#2f97d4;
    --green:#7cc242;
    --band:#5c88aa;
    --ink:#505459;
    --paper:#ffffff;
    --backdrop:#e4e5e6;
  }
  *{margin:0;padding:0;box-sizing:border-box}
  html,body{width:1200px;height:912px;overflow:hidden;background:var(--backdrop)}
  body{font-family:"Source Sans 3",Arial,sans-serif;color:var(--ink);position:relative}
  .spread{position:absolute;left:82px;top:110px;width:1016px;height:658px;background:var(--paper)}
  .page{position:absolute;top:0;width:508px;height:658px}
  .page--left{left:0}
  .page--right{left:508px}
  .brand{position:absolute;top:30px;color:var(--navy);font-weight:700;line-height:1;display:flex;align-items:center;gap:5px}
  .brand__square{width:14px;height:14px;background:var(--navy)}
  .brand__name{display:flex;flex-direction:column;font-size:16px;letter-spacing:.5px}
  .brand__name small{font-size:7.4px;letter-spacing:.2px}
  .page--left .brand{left:36px}
  .page--right .brand{right:36px}
  .running-head{position:absolute;top:39px;font-size:10.5px;font-weight:700;color:#2f3338}
  .page--left .running-head{right:37px}
  .page--right .running-head{left:36px}
  .tab-marker{position:absolute;left:483px;top:37px;width:50px;height:20px;background:var(--green)}
  .hero{position:absolute;left:0;top:74px;width:508px;height:190px}
  .hero__photo{position:absolute;left:0;top:63px;width:508px;height:127px;background:linear-gradient(135deg,#4f7fb0 0%,#9fb8cc 45%,#c7a24a 70%,#3e6a93 100%)}
  .hero__title{position:absolute;right:62px;top:38px;font-family:"Fira Sans Extra Condensed","Arial Narrow",sans-serif;font-weight:600;font-size:23px;color:#fff;letter-spacing:.2px}
  .intro{position:absolute;left:36px;top:295px;width:436px;font-size:9.6px;line-height:12.2px}
  .intro strong{color:var(--navy)}
  .lead{position:absolute;left:36px;top:398px;font-size:9.4px}
  .service{position:absolute}
  .service h3{font-size:11px;font-weight:700;color:var(--navy);margin-bottom:3px}
  .service ul{list-style:none}
  .service li{font-size:9.2px;line-height:15.3px;padding-left:12px;position:relative}
  .service li::before{content:"+";position:absolute;left:0;top:0;color:var(--sky);font-weight:700}
  .service li.wrap{line-height:15.3px}
  .service--vacuum{left:36px;top:426px}
  .service--hydro{left:271px;top:426px}
  .service--facility{left:36px;top:97px;width:240px}
  .service--product{left:257px;top:308px}
  .col-shadow{position:absolute;left:248px;top:420px;width:6px;height:160px;background:linear-gradient(90deg,rgba(0,0,0,.04),rgba(0,0,0,0))}
  .photo{position:absolute}
  .photo--truck{left:286px;top:85px;width:222px;height:196px;background:linear-gradient(180deg,#5b9ad8 0%,#8fbde6 40%,#dfe2df 60%,#b8a98c 100%)}
  .photo--worker{left:0;top:290px;width:241px;height:257px;background:linear-gradient(150deg,#9a4a32 0%,#d35a2c 45%,#7b7d80 100%)}
  .photo--blaster{left:241px;top:458px;width:267px;height:149px;background:linear-gradient(160deg,#8e8a80 0%,#c9c4b6 45%,#d6c24a 70%,#6d6a63 100%)}
  .footer{position:absolute;left:0;top:615px;width:1016px;height:23px}
  .footer__url{position:absolute;top:619px;width:508px;text-align:center;font-size:12.5px;letter-spacing:2.4px;color:#fff}
  .footer__url b{font-weight:700}
  .footer__url--left{left:0}
  .footer__url--right{left:0}
</style>
</head>
<body>
<main class="spread">
  <svg class="footer" width="1016" height="23" viewBox="0 0 1016 23" aria-hidden="true">
    <rect width="1016" height="23" fill="var(--band)"/>
    <polygon points="0,0 80,0 58,23 0,23" fill="var(--navy)"/>
    <polygon points="950,0 1016,0 1016,23 928,23" fill="var(--navy)"/>
  </svg>
  <div class="tab-marker"></div>

  <section class="page page--left">
    <div class="brand"><span class="brand__square"></span><span class="brand__name">KDL<small>ENVIRONMENTAL</small></span></div>
    <p class="running-head">Services We Provide</p>

    <div class="hero">
      <div class="hero__photo" role="img" aria-label="Photo of an industrial plant with steel piping, stairways and yellow railings under a blue sky"></div>
      <svg width="508" height="190" viewBox="0 0 508 190" style="position:absolute;left:0;top:0" aria-hidden="true">
        <defs>
          <linearGradient id="bannerFill" x1="0" y1="0" x2="1" y2="0">
            <stop offset="0" stop-color="#1b4f8c"/>
            <stop offset="1" stop-color="#2a6db1"/>
          </linearGradient>
        </defs>
        <polygon points="0,0 508,0 508,84 196,84 176,63 0,63" fill="url(#bannerFill)"/>
        <polygon points="300,0 395,0 408,10 313,10" fill="var(--sky)"/>
        <polygon points="135,63 168,63 190,88 157,88" fill="var(--green)"/>
        <polygon points="0,63 140,63 150,70 0,70" fill="var(--sky)" opacity=".7"/>
      </svg>
      <h1 class="hero__title">INDUSTRIAL SERVICES</h1>
    </div>

    <p class="intro"><strong>KDL's Industrial Services Division</strong> is the hardest working team in the business. We're at work 24 hours a day, 365 days a year in a diverse array of facilities across the Southeast. For over 20 years, we've been safely and efficiently performing all facets of industrial cleaning. With the equipment of a large company and the attention to detail of a small one, KDL gets the job done right the first time, every time. Partnering with us translates to "peace of mind." No more worrying that the job will be done on time. No more worrying about accidents. No more worrying about hidden fees or the dreaded "change order." Just your project done right.</p>
    <p class="lead">Here's a partial overview of our capabilities:</p>

    <div class="col-shadow"></div>
    <div class="service service--vacuum">
      <h3>Vacuum Truck Service</h3>
      <ul>
        <li>Sump/ Pit Cleaning</li>
        <li>Oil-water separator cleaning and maintenance</li>
        <li>Bulk solids and ash handling</li>
        <li>Aggressive Fluid Vapor Recovery</li>
        <li>Liquids vacuum transfer and removal</li>
        <li>Liquids and solids transportation</li>
      </ul>
    </div>
    <div class="service service--hydro">
      <h3>Hydroblasting Services</h3>
      <ul>
        <li>No entry (3D tool) tank cleaning</li>
        <li>Interior and Exterior surface cleaning</li>
        <li>Tanks, reactor, and vessel cleaning</li>
        <li>Tube and process pipe "lancing"</li>
        <li>Boilers, ships, barges, and railcars, etc.</li>
        <li>Evaporator and heat exchanger cleaning</li>
        <li>Unclogging drainage lines</li>
        <li>Facility decontamination</li>
      </ul>
    </div>
    <p class="footer__url footer__url--left">www.<b>kdlpurex</b>.com</p>
  </section>

  <section class="page page--right">
    <p class="running-head">Services We Provide</p>
    <div class="brand"><span class="brand__square"></span><span class="brand__name">KDL<small>ENVIRONMENTAL</small></span></div>

    <div class="service service--facility">
      <h3>Facility Maintenance and Cleaning Services</h3>
      <ul>
        <li>Tank and Line Cleaning</li>
        <li>Scheduled/Emergency plant shut downs</li>
        <li>Cooling towers</li>
        <li>Drain and sump cleanout</li>
        <li>Oil-water separators</li>
        <li>Confined Space Entry</li>
        <li class="wrap">No dig utilities excavation with hydroexcavation and pneunoexcavation</li>
        <li>Pond/ lagoon cleaning and dredging</li>
        <li>High Temperature Access</li>
      </ul>
    </div>
    <div class="photo photo--truck" role="img" aria-label="Photo of a white vacuum truck with blue tanks parked on a gravel work site"></div>
    <div class="photo photo--worker" role="img" aria-label="Photo of a worker in an orange protective suit and respirator entering a vessel manway"></div>
    <div class="service service--product">
      <h3>Product Handling</h3>
      <ul>
        <li>Hazardous and Non-Hazardous Material Removal</li>
        <li>Product Transfer</li>
        <li>Solidification</li>
        <li>Stabilization</li>
        <li>Product recovery and recycling</li>
        <li>Wastewater Treatment</li>
        <li>Waste Transportation</li>
      </ul>
    </div>
    <div class="photo photo--blaster" role="img" aria-label="Photo of a worker in yellow rain gear hydroblasting the inside of a concrete tank"></div>
    <p class="footer__url footer__url--right">www.<b>kdlpurex</b>.com</p>
  </section>
</main>
</body>
</html>
```